Bodywork Quietude Business Card Design

I want to create a very elegant and sophisticated two sided business card for my massage practice (www.bodyworkquietude.net). I have attached the logo and a PDF with some ideas down for the back of the card but I am open to suggestions. I will want to tie in a post card and flyer to the card later.
Similar colors to website would be great.
Target Market(s)
High end clientele, people looking for a sophisticated spa experience.
Industry/Entity Type
Massage
Contact Information for Business Card
Bodywork Quietude
7318 Larkspur Ave S, Suite 305
Seattle, WA 98103
(206) 555-0147
www.bodyworkquietude.net
Look and feel

```html
<!DOCTYPE html>
<html lang="en">
<head>
<meta charset="utf-8">
<title>Bodywork Quietude Business Card</title>
<link href="https://fonts.googleapis.com/css2?family=EB+Garamond:ital,wght@0,400;1,400&family=Roboto:wght@400;500;700&display=swap" rel="stylesheet">
<style>
  :root {
    --backdrop: #5a4838;
    --navy: #1b3140;
    --paper: #f2f2f1;
    --arc-grey: #8a8a8a;
    --ink-white: #ffffff;
  }
  html, body {
    margin: 0;
    padding: 0;
    width: 1200px;
    height: 960px;
    overflow: hidden;
    background: var(--backdrop);
  }
  .card {
    position: absolute;
    border-radius: 18px;
    overflow: hidden;
  }
  .card-front {
    left: 314px;
    top: 113px;
    width: 602px;
    height: 343px;
    background: var(--paper);
  }
  .card-front .front-shapes {
    position: absolute;
    inset: 0;
  }
  .brand-name {
    position: absolute;
    left: 20px;
    top: 253px;
    width: 276px;
    margin: 0;
    text-align: center;
    font-family: "EB Garamond", serif;
    font-weight: 400;
    font-size: 21px;
    letter-spacing: 0.5px;
    color: var(--navy);
    white-space: nowrap;
  }
  .card-front .brand-name { top: 140px; }
  .holder {
    position: absolute;
    right: 39px;
    top: 40px;
    text-align: right;
    font-family: "Roboto", sans-serif;
    color: var(--ink-white);
  }
  .holder-name {
    margin: 0;
    font-size: 20px;
    font-weight: 700;
    line-height: 24px;
  }
  .holder-title {
    margin: 0;
    font-size: 14px;
    font-weight: 500;
    line-height: 20px;
  }
  .contact {
    position: absolute;
    right: 39px;
    top: 204px;
    text-align: right;
    font-family: "Roboto", sans-serif;
    font-size: 14px;
    line-height: 18px;
    color: var(--ink-white);
    font-style: normal;
  }
  .contact p { margin: 0; }
  .contact .lines { margin-bottom: 10px; }
  .contact .with-icon {
    display: flex;
    justify-content: flex-end;
    align-items: center;
    gap: 5px;
    margin-bottom: 1px;
  }
  .contact svg { width: 12px; height: 12px; }
  .card-back {
    left: 311px;
    top: 472px;
    width: 600px;
    height: 342px;
    background: var(--navy);
    color: var(--ink-white);
    font-family: "EB Garamond", serif;
    font-style: italic;
    font-size: 22px;
    line-height: 28px;
    text-align: center;
  }
  .card-back p { margin: 0; }
  .back-intro { margin-top: 60px !important; }
  .back-services { margin-top: 20px !important; }
  .back-callout { margin-top: 22px !important; }
</style>
</head>
<body>
  <section class="card card-front">
    <svg class="front-shapes" viewBox="0 0 602 343" width="602" height="343">
      <path d="M211 0 C 330 60, 372 220, 276 343 L602 343 L602 0 Z" fill="var(--arc-grey)"/>
      <path d="M276 0 C 352 60, 372 210, 276 343 L602 343 L602 0 Z" fill="var(--navy)" stroke="#ffffff" stroke-width="2"/>
    </svg>
    <p class="brand-name">BODYWORK QUIETUDE</p>
    <div class="holder">
      <p class="holder-name">DANIEL HARTWELL</p>
      <p class="holder-title">CEO/FOUNDER</p>
    </div>
    <address class="contact">
      <div class="lines">
        <p>7318 Larkspur Ave S</p>
        <p>Suite 305</p>
        <p>Seattle, WA 98103</p>
      </div>
      <p class="with-icon">(206) 555-0147
        <svg viewBox="0 0 24 24"><path fill="#fff" d="M6.6 10.8a15 15 0 0 0 6.6 6.6l2.2-2.2a1 1 0 0 1 1-.25 11.4 11.4 0 0 0 3.6.57 1 1 0 0 1 1 1V20a1 1 0 0 1-1 1A17 17 0 0 1 3 4a1 1 0 0 1 1-1h3.5a1 1 0 0 1 1 1c0 1.25.2 2.45.57 3.57a1 1 0 0 1-.25 1z"/></svg>
      </p>
      <p class="with-icon">bodyworkquietude.net
        <svg viewBox="0 0 24 24"><circle cx="12" cy="12" r="10" fill="none" stroke="#fff" stroke-width="2.4"/><path d="M2 12h20M12 2c3 3 3 17 0 20M12 2c-3 3-3 17 0 20" fill="none" stroke="#fff" stroke-width="2"/></svg>
      </p>
    </address>
  </section>

  <section class="card card-back">
    <p class="back-intro">Experience the Most Unique,<br>Relaxing and Invitingly Deep<br>Massage of Your Life.....</p>
    <p class="back-services">Deep Lomi | Ultra Relaxation<br>Nurturing Touch | Cupping<br>Thai Yoga Massage | Couple’s Massage</p>
    <p class="back-callout">We Make House Calls</p>
  </section>
</body>
</html>
```